Professional looking website for solo practitioner law practice

I have recently started up my new law practice. Currently there is just myself practicing here. I would like to have a website that provides my contact information, a map, and the different areas of law that I practice in, being Family Litigation, Wills & Estates, Corporate/Commerical, and Real Estate. I recently had a logo designed so I would like the colours of my website to be congruent with that and include the logo.
I am located in Edmonton, Alberta.

Reason: I will be away for the next few days.

Target Market(s)

individuals and families with an income of $50K+, mostly those looking for family lawyer re divorce, child support, custody and parenting, spousal support.

Industry/Entity Type

Lawyer

Number of Pages Required

4 page

Font styles to use
Serif

Colors
0355a3

Requirements
Must have
• Contact information, ability to email me, background picture(s) that are professional and fit with the legal services theme/service provided but are not single individual lawyers, gavels, or court houses. Need to have click to change the text to include information on Family Litigation, Wills & Estates, Corporate/Commercial, and Real Estate
Nice to have
• contact box
Should not have
• blog, sans serif text, testimonials, news

```html
<!DOCTYPE html>
<html lang="en">
<head>
<meta charset="utf-8">
<title>Marlow Keane Law Office</title>
<link href="https://fonts.googleapis.com/css2?family=Cinzel:wght@400;700&family=Crimson+Text:wght@400;600&display=swap" rel="stylesheet">
<style>
:root{
  --brand:#0355a3;
  --brand-dark:#1c2f6b;
  --ink:#222;
  --body:#555;
  --light-bg:#f2f2f2;
  --rule:#d8d8d8;
  --footer:#000;
  --footer-field:#262626;
  --map-land:#dfe4e8;
  --map-road:#ffffff;
}
*{box-sizing:border-box;margin:0;padding:0}
html,body{width:718px;height:1200px;overflow:hidden;background:#fff}
body{position:relative;font-family:'Crimson Text',Georgia,serif;color:var(--body)}
.abs{position:absolute}

/* hero */
.hero{left:0;top:0;width:718px;height:325px;background:linear-gradient(100deg,#d9dad6 0%,#9c9a96 25%,#cfc6bd 48%,#b8b4b0 62%,#dfe3e8 80%,#c9ccd0 100%)}
.nav{left:59px;top:14px;width:599px;height:42px;background:rgba(255,255,255,.94);border-bottom:1px solid var(--brand-dark)}
.brand{left:8px;top:8px;display:flex;align-items:center;gap:6px}
.brand-square{width:28px;height:28px;border:2px solid var(--brand-dark)}
.brand-name{font-family:'Cinzel',Georgia,serif;font-size:14px;color:var(--brand-dark);line-height:1}
.brand-sub{font-family:'Cinzel',Georgia,serif;font-size:6px;letter-spacing:2px;color:var(--brand-dark);margin-top:2px}
.nav-item{top:0;height:36px;line-height:38px;font-family:'Cinzel',Georgia,serif;font-size:8px;color:#111}
.nav-item.active{background:var(--brand);color:#fff;text-align:center;width:37px}
.caption{left:59px;top:290px;width:599px;height:35px;background:rgba(30,30,30,.78)}
.caption-text{left:12px;top:9px;font-family:'Cinzel',Georgia,serif;font-size:14px;color:#fff;letter-spacing:.5px}
.dot{width:5px;height:5px;top:17px;background:#777}
.dot.on{background:#fff}

/* section headings */
.heading{font-family:'Cinzel',Georgia,serif;font-size:13px;color:var(--ink);letter-spacing:.3px}
.heading .accent{color:var(--brand)}
.bracket{height:7px;border:1px solid var(--brand)}
.bracket.top{border-bottom:none}
.bracket.bottom{border-top:none}
.para{font-size:9px;line-height:16.4px;color:var(--body)}
.btn{background:var(--brand);color:#fff;font-family:'Cinzel',Georgia,serif;font-size:8px;text-align:center;line-height:22px;height:22px;border-bottom:2px solid #022d57}

/* about */
.mark-box{left:69px;top:352px;width:128px;height:128px;border:6px solid #e2e2e2;display:flex;align-items:center;justify-content:center;text-align:center;font-family:'Cinzel',Georgia,serif;font-size:17px;color:#dcdcdc;line-height:1.2}

/* practice */
.practice{left:0;top:505px;width:470px;height:295px;background:var(--light-bg)}
.practice-photo{left:470px;top:505px;width:248px;height:295px;background:linear-gradient(160deg,#eef1f5 0%,#c9cdd3 35%,#8d8a8c 60%,#3a3a3e 85%,#2a2a2e 100%)}
.area{left:98px;font-family:'Cinzel',Georgia,serif;font-size:8px;line-height:12px;color:#111}
.area.current{color:var(--brand)}
.area-icon{left:63px}
.divider-v{left:172px;top:600px;width:1px;height:163px;background:var(--rule)}

/* location */
.location-pin{left:64px;top:884px}
.location-text{left:102px;top:884px;width:328px;font-size:9.5px;line-height:14px;color:#444}
.location-label{left:103px;top:962px;font-family:'Cinzel',Georgia,serif;font-size:8px;color:var(--brand)}
.office-map{left:463px;top:880px;width:190px;height:92px;background:var(--map-land);border:1px solid var(--rule);overflow:hidden}

/* footer */
.footer{left:0;top:1009px;width:718px;height:191px;background:var(--footer)}
.foot-title{font-family:'Cinzel',Georgia,serif;font-size:11px;color:#fff;top:1033px;letter-spacing:.3px}
.foot-link{left:60px;font-family:'Cinzel',Georgia,serif;font-size:7px;color:#999}
.field{background:var(--footer-field);font-size:7.5px;color:#888;padding:4px 5px}
.foot-info{left:387px;font-size:8px;line-height:13px;color:#ddd}
.world-map{left:420px;top:1055px;width:110px;height:70px;background:radial-gradient(ellipse at center,#1e1e1e 0%,#000 75%)}
.social{top:1120px;width:15px;height:15px}
.foot-mark{left:573px;top:1052px;width:76px;height:76px;border:3px solid #555;display:flex;align-items:center;justify-content:center;text-align:center;font-family:'Cinzel',Georgia,serif;font-size:10px;color:#666;line-height:1.2}
.foot-rule{left:0;top:1173px;width:718px;height:1px;background:#1a1a1a}
.copyright{left:0;top:1180px;width:718px;text-align:center;font-size:8px;color:#888}
</style>
</head>
<body>

<!-- hero -->
<div class="abs hero" role="img" aria-label="Photo of a lawyer reviewing a tablet with a smiling couple in a bright office"></div>
<nav class="abs nav">
  <div class="abs brand">
    <div class="brand-square"></div>
    <div><div class="brand-name">Marlow Keane</div><div class="brand-sub">LAW OFFICE</div></div>
  </div>
  <div class="abs nav-item active" style="left:231px">Home</div>
  <div class="abs nav-item" style="left:287px">Abouts Us</div>
  <div class="abs nav-item" style="left:368px">Ractice Areas</div>
  <div class="abs nav-item" style="left:454px">Testimonial</div>
  <div class="abs nav-item" style="left:534px">Contact Us</div>
</nav>
<div class="abs caption">
  <div class="abs caption-text">Courage To Fail, Wisdom To Succeed</div>
  <div class="abs dot on" style="left:553px"></div>
  <div class="abs dot" style="left:561px"></div>
  <div class="abs dot" style="left:569px"></div>
</div>

<!-- about -->
<div class="abs mark-box">Marlow<br>Keane</div>
<div class="abs bracket top" style="left:231px;top:350px;width:36px"></div>
<div class="abs heading" style="left:230px;top:358px">About <span class="accent">Marlow Keane law office</span></div>
<div class="abs bracket bottom" style="left:231px;top:372px;width:36px"></div>
<p class="abs para" style="left:230px;top:386px;width:430px">Lorem Ipsum is simply dummy text of the printing and typesetting industry. Lorem Ipsum has been t industry's standard dummy text ever since the 1500s, when an unknown printer took a galley of type and scrambled it tol make a type specimen book. It has survived not only, but also the lea&nbsp; Remaining essentially unchanged. It was including versions of survived Lorem&nbsp; Remaining...</p>
<div class="abs btn" style="left:229px;top:459px;width:73px">Read More</div>

<!-- practice -->
<section class="abs practice"></section>
<div class="abs practice-photo" role="img" aria-label="Photo of three colleagues working together at a laptop in a meeting room"></div>
<div class="abs bracket top" style="left:62px;top:531px;width:28px"></div>
<div class="abs heading" style="left:61px;top:540px">Practise <span class="accent">Area</span></div>
<div class="abs bracket bottom" style="left:62px;top:553px;width:28px"></div>
<p class="abs para" style="left:60px;top:570px;font-size:8.5px">Simply dummy text of the printing and typesetting industry Lorem Ipsum has been the industry's...</p>

<svg class="abs area-icon" style="top:615px" width="18" height="18" viewBox="0 0 18 18" fill="#0355a3"><circle cx="5.5" cy="3" r="2.3"/><circle cx="12.5" cy="3" r="2.3"/><path d="M2.5 6.5h6v6h-1v5h-4v-5h-1zM9.5 6.5h6v6h-1v5h-4v-5h-1z"/></svg>
<div class="abs area current" style="top:614px">Family<br>Litigation</div>
<svg class="abs area-icon" style="top:657px" width="20" height="20" viewBox="0 0 20 20" fill="none" stroke="#0355a3" stroke-width="1.6"><rect x="2" y="2" width="12" height="16"/><path d="M5 6h6M5 9h6M5 12h4M11 15l7-9"/></svg>
<div class="abs area" style="top:657px">Wills &amp;<br>Estates</div>
<svg class="abs area-icon" style="top:701px" width="22" height="18" viewBox="0 0 22 18" fill="none" stroke="#0355a3" stroke-width="1.6"><rect x="1" y="4" width="20" height="13" rx="1"/><path d="M8 4V1h6v3M1 9h20"/></svg>
<div class="abs area" style="top:701px">Corporate/<br>Commercial</div>
<svg class="abs area-icon" style="top:741px" width="22" height="16" viewBox="0 0 22 16" fill="#0355a3"><path d="M2 8l8-7 8 7h-3v4H5V8z"/><path d="M0 14c5-3 9-1 13 0s7-1 9-3v5H0z"/></svg>
<div class="abs area" style="top:745px">Real Estate</div>

<div class="abs divider-v"></div>
<svg class="abs" style="left:172px;top:612px" width="5" height="10" viewBox="0 0 5 10"><path d="M0 0l5 5-5 5z" fill="#0355a3"/></svg>
<div class="abs heading" style="left:192px;top:614px;color:var(--brand)">Family Litigation</div>
<p class="abs para" style="left:193px;top:632px;width:268px">Remaining essentially unchanged text of the printing and typesetting industry. Lorem Ipsum has been t industry's standard dummy text ever since the 1500s, when an unknown printer took a galley of type and scrambled it tol make a type specimen book. It has survived not only, but also the lea&nbsp; Remaining essentially unchanged. It was including versions of survived Lorem&nbsp; Remaining...</p>
<div class="abs btn" style="left:193px;top:740px;width:73px">Read More</div>

<!-- location -->
<div class="abs bracket top" style="left:287px;top:834px;width:60px"></div>
<div class="abs heading" style="left:0;width:718px;text-align:center;top:841px">Find <span class="accent">Our Office</span></div>
<div class="abs bracket bottom" style="left:287px;top:855px;width:60px"></div>
<svg class="abs location-pin" width="24" height="32" viewBox="0 0 24 32"><path d="M12 0C5.4 0 0 5.4 0 12c0 9 12 20 12 20s12-11 12-20C24 5.4 18.6 0 12 0z" fill="#0355a3"/><circle cx="12" cy="12" r="4.5" fill="#fff"/></svg>
<p class="abs location-text">Our office is located in Edmonton, Alberta, and welcomes individuals and families by appointment. We offer a confidential first meeting to discuss divorce, child support, custody and parenting, spousal support, wills and estates, corporate and commercial matters, and real estate transactions. Free parking is available next to the building.</p>
<div class="abs location-label">Monday – Friday, 9:00 – 5:00</div>
<div class="abs" style="left:445px;top:875px;width:1px;height:97px;background:var(--rule)"></div>
<div class="abs office-map" role="img" aria-label="Street map showing the office location in Edmonton">
  <svg width="190" height="92" viewBox="0 0 190 92">
    <path d="M0 30h190M0 66h190M48 0v92M120 0v92M0 88L190 8" stroke="#fff" stroke-width="4" fill="none"/>
    <path d="M95 34c-5 0-9 4-9 9 0 7 9 15 9 15s9-8 9-15c0-5-4-9-9-9z" fill="#0355a3"/>
    <circle cx="95" cy="43" r="3.2" fill="#fff"/>
  </svg>
</div>

<!-- footer -->
<footer class="abs footer"></footer>
<div class="abs foot-title" style="left:60px">Quick Link</div>
<div class="abs foot-link" style="top:1060px">- Home</div>
<div class="abs foot-link" style="top:1081px">- About Us</div>
<div class="abs foot-link" style="top:1103px">- Practice Areas</div>
<div class="abs foot-link" style="top:1124px">- Contact Us</div>

<div class="abs foot-title" style="left:157px">Quick Contact</div>
<div class="abs field" style="left:157px;top:1059px;width:97px;height:18px">Name</div>
<div class="abs field" style="left:157px;top:1079px;width:97px;height:18px">Email</div>
<div class="abs field" style="left:157px;top:1100px;width:97px;height:18px">Phone</div>
<div class="abs field" style="left:258px;top:1059px;width:106px;height:59px">Massage</div>
<div class="abs btn" style="left:157px;top:1123px;width:55px;height:17px;line-height:17px;border:none">Submit</div>

<div class="abs world-map" role="img" aria-label="Faint dotted world map"></div>
<div class="abs foot-title" style="left:387px">Contact Info</div>
<div class="abs foot-info" style="top:1054px">1234 Street Name, City Name,<br>United States</div>
<div class="abs foot-info" style="top:1084px">Phone : +123 456 7890<br>Email : info@marlowkeanelaw.example</div>
<div class="abs social" style="left:388px;background:#3b5998" role="img" aria-label="Social link"></div>
<div class="abs social" style="left:410px;background:#1da1f2" role="img" aria-label="Social link"></div>
<div class="abs social" style="left:432px;background:#0e76a8" role="img" aria-label="Social link"></div>
<div class="abs social" style="left:454px;background:#dd4b39" role="img" aria-label="Social link"></div>

<div class="abs foot-mark">Marlow<br>Keane</div>
<div class="abs foot-rule"></div>
<div class="abs copyright">Copyright &copy; 2016 - Marlow Keane law office, All Rights Reserved</div>

</body>
</html>
```